Microlight Aircraft Website Project

Need a website designed, or at least a template made, that my web programmer can work with here. We are a new manufacturer of microlight aircraft & powered hang gliders. Our company name is Brisk Tern. We manufacture portable utility aircraft in the Light Sport category (formerly known as Ultralights or Microlights). Our particular design is a 2-seat powered hang glider and caters to those who want to go explore the backcountry. We are not necessarily aviation nuts, but more into the development of a flying utility vehicle for extreme exploration and expeditions. We have been importing these aircraft from 3 countries for 15 years and have supplied over 200 expedition-quality aircraft world-wide. We are now manufacturing here in the US.

Industry/Entity Type

Manufacturer

Coding

Coded - Design and coding required

```html
<!DOCTYPE html>
<html lang="en">
<head>
<meta charset="utf-8">
<title>Brisk Tern — Microlight Aircraft</title>
<link href="https://fonts.googleapis.com/css2?family=Open+Sans:wght@400;600;700;800&family=Lato:wght@400;700&display=swap" rel="stylesheet">
<style>
  :root {
    --blue: #3a5fb4;
    --blue-dark: #2d4a94;
    --ink: #333;
    --muted: #6b6b6b;
    --rule: #b8b8b8;
    --light: #f4f4f4;
    --footer: #2b2b2b;
    --footer-base: #1f1f1f;
    --white: #fff;
  }
  * { box-sizing: border-box; margin: 0; padding: 0; }
  html, body { width: 1200px; height: 3211px; overflow: hidden; }
  body { position: relative; background: var(--white); font-family: "Lato", sans-serif; color: var(--ink); }
  .abs { position: absolute; }

  /* header */
  .site-header { position: absolute; top: 0; left: 0; width: 1200px; height: 80px; background: var(--white); }
  .brand { position: absolute; left: 118px; top: 22px; display: flex; align-items: center; gap: 10px;
    font-family: "Open Sans", sans-serif; font-weight: 700; font-size: 22px; color: var(--blue-dark); }
  .brand-mark { width: 14px; height: 14px; background: var(--blue-dark); }
  .main-nav { position: absolute; left: 498px; top: 0; display: flex; height: 80px; }
  .main-nav a { display: flex; align-items: center; padding: 0 16px; height: 80px; font-size: 13px; color: var(--ink); text-decoration: none; }
  .main-nav a.is-active { background: var(--blue); color: var(--white); }

  /* hero */
  .hero { position: absolute; top: 80px; left: 0; width: 1200px; height: 476px;
    background: linear-gradient(160deg, #8fa3b8 0%, #4d6a5a 35%, #1f5a8a 65%, #103a6e 100%); }
  .hero-title { position: absolute; left: 493px; top: 150px; font-family: "Open Sans", sans-serif; font-weight: 700; font-size: 70px; color: var(--white); letter-spacing: 1px; }
  .hero-sub { position: absolute; left: 494px; top: 250px; font-family: "Open Sans", sans-serif; font-weight: 700; font-size: 27px; color: var(--white); }
  .hero-dots { position: absolute; left: 537px; top: 449px; display: flex; gap: 8px; }
  .hero-dots span { width: 50px; height: 5px; background: rgba(255,255,255,.8); }
  .hero-dots span.is-current { background: var(--blue); }

  .rule { position: absolute; width: 54px; height: 3px; background: var(--rule); }
  .section-title { position: absolute; font-family: "Open Sans", sans-serif; font-weight: 700; font-size: 31px; color: var(--blue-dark); }

  /* welcome */
  .welcome-text { position: absolute; left: 211px; top: 703px; width: 789px; text-align: center; font-size: 12.5px; line-height: 21px; color: var(--muted); }
  .photo { position: absolute; }

  /* microlight band */
  .microlight-band { position: absolute; top: 1573px; left: 0; width: 1200px; height: 425px; background: var(--blue); }
  .band-title { position: absolute; font-family: "Open Sans", sans-serif; font-weight: 700; font-size: 29px; color: var(--white); }
  .band-text { position: absolute; font-size: 12.5px; line-height: 22px; color: var(--white); }
  .btn { position: absolute; display: flex; align-items: center; justify-content: center; font-size: 12px; font-weight: 700; border-radius: 3px; }
  .btn-light { border: 1.5px solid var(--white); color: var(--white); }
  .btn-blue { border: 1.5px solid var(--blue); color: var(--blue); background: var(--white); }

  .body-text { position: absolute; font-size: 12.5px; line-height: 22px; color: var(--muted); }
  .body-text b { color: var(--ink); }

  /* contact band */
  .contact-band { position: absolute; top: 2429px; left: 0; width: 1200px; height: 113px; background: var(--blue); }
  .contact-title { position: absolute; left: 322px; top: 26px; font-family: "Open Sans", sans-serif; font-weight: 600; font-size: 29px; color: var(--white); }
  .contact-sub { position: absolute; left: 322px; top: 64px; font-size: 21px; color: var(--white); }

  /* testimonial */
  .quote-box { position: absolute; left: 113px; top: 2673px; width: 476px; height: 149px; background: var(--light); }
  .quote-mark { position: absolute; font-family: "Open Sans", sans-serif; font-size: 48px; color: #bbb; line-height: 1; }
  .quote-text { position: absolute; left: 30px; top: 26px; width: 416px; text-align: center; font-size: 12.5px; line-height: 21px; color: var(--muted); }
  .avatar { position: absolute; left: 164px; top: 2851px; width: 63px; height: 63px; border-radius: 50%; background: linear-gradient(135deg, #c8a48c, #7a5a48); }
  .person-name { position: absolute; left: 256px; top: 2856px; font-size: 14px; font-weight: 700; color: var(--blue); }
  .person-role { position: absolute; left: 256px; top: 2881px; font-size: 12.5px; color: var(--muted); }
  .slider-arrow { position: absolute; top: 2849px; width: 22px; height: 22px; display: flex; align-items: center; justify-content: center; }

  /* footer */
  .site-footer { position: absolute; top: 3022px; left: 0; width: 1200px; height: 144px; background: var(--footer); color: #ddd; }
  .footer-col { position: absolute; top: 35px; font-size: 12px; }
  .footer-col h4 { font-size: 12px; font-weight: 700; color: var(--white); margin-bottom: 16px; text-transform: uppercase; }
  .footer-col p { line-height: 27px; display: flex; align-items: center; gap: 8px; }
  .social { display: flex; gap: 7px; }
  .social span { width: 29px; height: 29px; background: #e8e8e8; }
  .footer-base { position: absolute; top: 3166px; left: 0; width: 1200px; height: 45px; background: var(--footer-base);
    color: #ddd; font-size: 12px; display: flex; align-items: center; justify-content: center; }
  .to-top { position: absolute; right: 40px; top: 11px; width: 24px; height: 24px; border-radius: 50%; background: #3a3a3a; display: flex; align-items: center; justify-content: center; }
</style>
</head>
<body>

<header class="site-header">
  <div class="brand"><span class="brand-mark"></span>Brisk Tern</div>
  <nav class="main-nav">
    <a class="is-active">Home</a>
    <a>About us</a>
    <a>Microlights</a>
    <a>Hang glider</a>
    <a>Spare parts</a>
    <a>Gallery</a>
    <a>Contact us</a>
  </nav>
</header>

<section class="hero" role="img" aria-label="Yellow microlight trike flying over a blue mountain lake and forested shoreline">
  <h1 class="hero-title">DON'T MISS OUT</h1>
  <p class="hero-sub">ON THE THRILL OF A LIFETIME!</p>
  <div class="hero-dots"><span></span><span class="is-current"></span><span></span></div>
</section>

<div class="rule" style="left:573px;top:603px"></div>
<h2 class="section-title" style="left:0;width:1200px;text-align:center;top:628px">Welcome to Brisk Tern world</h2>
<p class="welcome-text">Lorem ipsum dolor sit amet, consectetur adipiscing elit, sed do eiusmod tempor incididunt ut labore et dolore magna aliqua. Ut enim ad minim veniam, quis nostrud exercitation ullamco laboris nisi ut aliquip ex ea commodo consequat. Duis aute irure dolor in reprehenderit in voluptate velit esse cillum dolore eu fugiat nulla pariatur. Excepteur sint occaecat cupidatat non proident, sunt in culpa qui officia deserunt mollit anim id est laborum.</p>

<div class="photo" style="left:113px;top:824px;width:307px;height:432px;background:linear-gradient(160deg,#a9c6e6,#e8c23a 60%,#9bb8d8)" role="img" aria-label="Yellow and blue microlight trike with two pilots in flight"></div>
<div class="photo" style="left:113px;top:1278px;width:307px;height:229px;background:linear-gradient(180deg,#c9d6e2,#a7b6c4 70%,#6d7f5a)" role="img" aria-label="Hang glider flying over a coastline"></div>
<div class="photo" style="left:447px;top:824px;width:306px;height:292px;background:linear-gradient(180deg,#4f6a4a,#7fa55a 55%,#8b8060)" role="img" aria-label="Green and white hang gliders on a grassy hilltop"></div>
<div class="photo" style="left:447px;top:1140px;width:306px;height:367px;background:linear-gradient(180deg,#b4c8de,#c94a3a 45%,#8fa6c0)" role="img" aria-label="Red microlight trike with pilot flying against a pale sky"></div>
<div class="photo" style="left:780px;top:824px;width:307px;height:225px;background:linear-gradient(180deg,#5e93d6,#b9d3ef 60%,#7a6a52)" role="img" aria-label="Colourful hang glider launching from a hill"></div>
<div class="photo" style="left:780px;top:1076px;width:307px;height:431px;background:linear-gradient(160deg,#9fc2e6,#e6c53a 50%,#a7c4e0)" role="img" aria-label="Yellow-wing microlight trike in flight"></div>

<section class="microlight-band">
  <div class="rule" style="left:113px;top:49px;background:#9fb3dd"></div>
  <h2 class="band-title" style="left:113px;top:72px">Microlight Aircraft</h2>
  <p class="band-text" style="left:113px;top:136px;width:470px">Built in the USA with the finest aircraft-quality materials available, Ridgeline Wing Light Sport Aircraft are known for their optimal combination of strong airframes, powerful and reliable engines, and outstanding wing performance. We have the right microlight trike and wing combination for you - on wheels, skis, or floats.</p>
  <div class="btn btn-light" style="left:113px;top:245px;width:94px;height:37px">Read more</div>
  <div class="photo" style="left:613px;top:80px;width:474px;height:258px;background:linear-gradient(180deg,#a8c4e4,#dde3e8 45%,#6e8a4a 70%,#4f6a34)" role="img" aria-label="Microlight trike parked on an airfield"></div>
</section>

<div class="photo" style="left:118px;top:2078px;width:464px;height:273px;background:linear-gradient(180deg,#c7d3de,#9aab9e 50%,#5c7a3e)" role="img" aria-label="Powered hang glider flying over a green valley"></div>
<div class="rule" style="left:613px;top:2046px"></div>
<h2 class="section-title" style="left:613px;top:2068px">Powered Hang Gliders</h2>
<p class="body-text" style="left:613px;top:2133px;width:474px"><b>Brisk Tern</b> hang gliders are designed to be easy-to-fly, built with quality hardware that reduces set-up time, and have a range of options and upgrades to customize your new glider. The Summit and Drift hang gliders are best for experienced skills, and the Breeze for all skill levels.</p>
<div class="btn btn-blue" style="left:613px;top:2244px;width:94px;height:37px">Read more</div>

<section class="contact-band">
  <h2 class="contact-title">Get In Touch</h2>
  <p class="contact-sub">For online appointment call us today!</p>
  <div class="btn btn-light" style="left:678px;top:38px;width:98px;height:37px">Contact us</div>
</section>

<div class="rule" style="left:113px;top:2592px"></div>
<h2 class="section-title" style="left:113px;top:2612px">Testimonials</h2>
<div class="quote-box">
  <span class="quote-mark" style="left:10px;top:4px">“</span>
  <p class="quote-text">Lorem ipsum dolor sit amet, consectetur adipiscing elit, sed do eiusmod tempor incididunt ut labore et dolore magna aliqua. Ut enim ad minim veniam, quis nostrud exercitation ullamco laboris nisi ut aliquip ex ea commodo consequat.</p>
  <span class="quote-mark" style="right:10px;bottom:-18px">”</span>
</div>
<div class="avatar" role="img" aria-label="Portrait photo of the reviewer"></div>
<div class="person-name">Mara Ellison</div>
<div class="person-role">Marketing director of Larkfield</div>
<div class="slider-arrow" style="left:536px;background:#777">
  <svg width="8" height="10" viewBox="0 0 8 10"><path d="M6 1 2 5l4 4" stroke="#fff" stroke-width="1.6" fill="none"/></svg>
</div>
<div class="slider-arrow" style="left:562px;background:var(--blue)">
  <svg width="8" height="10" viewBox="0 0 8 10"><path d="M2 1l4 4-4 4" stroke="#fff" stroke-width="1.6" fill="none"/></svg>
</div>

<div class="rule" style="left:613px;top:2592px"></div>
<h2 class="section-title" style="left:613px;top:2612px">Featured Video</h2>
<div class="photo" style="left:613px;top:2675px;width:474px;height:283px;background:linear-gradient(180deg,#3a3550,#b25a2a 50%,#7a3a1e)" role="img" aria-label="Video still of a microlight trike flying over red canyon rock formations">
  <svg class="abs" style="left:215px;top:119px" width="44" height="44" viewBox="0 0 44 44">
    <circle cx="22" cy="22" r="21" fill="rgba(0,0,0,.45)" stroke="#fff" stroke-width="2"/>
    <path d="M17 13v18l14-9z" fill="#fff"/>
  </svg>
</div>

<footer class="site-footer">
  <div class="footer-col" style="left:113px"><h4>Company info</h4><p>About us</p><p>Term &amp; Conditions</p></div>
  <div class="footer-col" style="left:360px"><h4>Company contact</h4>
    <p><svg width="12" height="10" viewBox="0 0 12 10"><rect x=".5" y=".5" width="11" height="9" fill="none" stroke="#ddd"/></svg>Lorem ipsum, ST 40512</p>
    <p><svg width="8" height="12" viewBox="0 0 8 12"><rect x=".5" y=".5" width="7" height="11" rx="1" fill="none" stroke="#ddd"/></svg>1-000-000-0000</p>
  </div>
  <div class="footer-col" style="left:613px"><h4>Support</h4><p>Call us</p><p>Email us</p></div>
  <div class="footer-col" style="left:862px"><h4>Get in touch</h4>
    <div class="social"><span></span><span></span><span></span><span></span><span></span></div>
  </div>
</footer>
<div class="footer-base">(c) Brisk Tern, 2016 All rights reserved
  <div class="to-top"><svg width="10" height="6" viewBox="0 0 10 6"><path d="M1 5l4-4 4 4" stroke="#ccc" stroke-width="1.5" fill="none"/></svg></div>
</div>

</body>
</html>
```